Valmo Sàrl - Business Card

VALMO Sàrl operates in the sector Services for banks and credit institutions. It is a B2B which connects companies. The main colors should be Blue and Black. The logo and look of the card should be simple, professional, conservative and reflect Connecting People.

Target Market(s)

Financial professionals and institutions

Industry/Entity Type

Finance

Contact Information for Business Card

Chemin des Vergers 9
1026 Denges

Logo Text

Joinpoint

Font styles to use
Serif
Sans Serif

Colors
0355a3
3176b5
85acd3
cfdeed

Requirements
Should not have
• Multiple colors

```html
<!DOCTYPE html>
<html lang="en">
<head>
<meta charset="utf-8">
<title>Valmo Sàrl – Business Card</title>
<link href="https://fonts.googleapis.com/css2?family=Montserrat:wght@400;500;600;700&display=swap" rel="stylesheet">
<style>
  :root {
    --blue: #0f72c0;
    --blue-deep: #0355a3;
    --band: #3a3a9e;
    --ink: #333333;
    --muted: #5a5a5a;
    --card-dark: #2e2e30;
    --card-dark-hi: #3c3c3f;
    --paper: #ffffff;
    --stage: #a9a9a9;
  }
  * { margin: 0; padding: 0; box-sizing: border-box; }
  html, body { width: 1200px; height: 930px; overflow: hidden; }
  body {
    background: var(--stage);
    font-family: "Montserrat", sans-serif;
    position: relative;
  }
  .card {
    position: absolute;
    width: 540px;
    height: 320px;
    border-radius: 22px;
    overflow: hidden;
    box-shadow: 0 6px 14px rgba(0,0,0,0.25);
  }
  .card-back {
    left: 70px;
    top: 110px;
    background: linear-gradient(160deg, var(--card-dark-hi), var(--card-dark));
    display: flex;
    align-items: center;
    justify-content: center;
  }
  .card-back .texture {
    position: absolute;
    inset: 0;
    background: radial-gradient(circle at 50% 50%, rgba(255,255,255,0.05), rgba(0,0,0,0) 70%);
  }
  .brand {
    display: flex;
    align-items: center;
    gap: 12px;
    font-weight: 700;
    letter-spacing: 1px;
    position: relative;
  }
  .brand-dot {
    width: 16px; height: 16px; border-radius: 50%;
  }
  .card-back .brand { color: #ffffff; font-size: 34px; }
  .card-back .brand-dot { background: #ffffff; }

  .card-front {
    left: 590px;
    top: 500px;
    background: var(--paper);
  }
  .front-band {
    position: absolute;
    left: 0; right: 0; bottom: 0;
    height: 16px;
    background: var(--band);
    border-top: 3px solid #1a1a1a;
  }
  .front-logo {
    position: absolute;
    left: 30px;
    top: 140px;
  }
  .front-logo .brand { color: var(--blue); font-size: 30px; }
  .front-logo .brand-dot { background: var(--blue); }
  .divider {
    position: absolute;
    left: 282px;
    top: 56px;
    width: 2px;
    height: 186px;
    background: var(--blue);
  }
  .contact {
    position: absolute;
    left: 304px;
    top: 48px;
    color: var(--ink);
    font-size: 13px;
    line-height: 1.45;
  }
  .person-name {
    color: var(--blue);
    font-size: 21px;
    font-weight: 600;
    line-height: 1.1;
  }
  .person-role { color: var(--muted); font-size: 14px; margin-bottom: 10px; }
  .address { font-size: 14px; margin-bottom: 6px; }
  .contact-line { display: flex; align-items: center; gap: 7px; }
  .contact-line svg { width: 11px; height: 11px; flex: none; }
  .contact-line .accent { color: var(--blue); font-weight: 600; }
</style>
</head>
<body>

  <section class="card card-back" aria-label="Business card back">
    <div class="texture" role="img" aria-label="subtle network line pattern on dark background"></div>
    <div class="brand"><span class="brand-dot"></span>JOINPOINT</div>
  </section>

  <section class="card card-front" aria-label="Business card front">
    <div class="front-logo">
      <div class="brand"><span class="brand-dot"></span>JOINPOINT</div>
    </div>
    <div class="divider"></div>
    <div class="contact">
      <div class="person-name">ADRIEN MOREL</div>
      <div class="person-role">President</div>
      <div class="address">Chemin des Vergers 9<br>1026 Denges</div>
      <div class="contact-line">
        <svg viewBox="0 0 12 12"><path d="M3 1l2 2.5-1.2 1.2a7 7 0 0 0 3.5 3.5L8.5 7 11 9l-1.2 2C5.5 11 1 6.5 1 2.2z" fill="#0f72c0"/></svg>
        021 555 01 42
      </div>
      <div class="contact-line">
        <svg viewBox="0 0 12 12"><rect x="1" y="2.5" width="10" height="7" fill="none" stroke="#0f72c0" stroke-width="1.2"/><path d="M1 3l5 3.5L11 3" fill="none" stroke="#0f72c0" stroke-width="1.2"/></svg>
        info@joinpoint.ch
      </div>
      <div class="contact-line">
        <svg viewBox="0 0 12 12"><circle cx="6" cy="6" r="5" fill="none" stroke="#0f72c0" stroke-width="1.1"/><ellipse cx="6" cy="6" rx="2.2" ry="5" fill="none" stroke="#0f72c0" stroke-width="1"/><path d="M1 6h10" stroke="#0f72c0" stroke-width="1"/></svg>
        <span>www.<span class="accent">joinpoint</span>.ch</span>
      </div>
    </div>
    <div class="front-band"></div>
  </section>

</body>
</html>
```